Redesign Company Website

Cellar Loop new website: www.cellarloop.com.au

Brief

• Cellar Loop
Cellar Loop is a relationship marketing company offering telesales services to partner wineries. We manage the winery’s database, engage in telesales campaigns and return great sales results to the winery.
Cellar Loop currently operates in Australia, New Zealand and Canada, with plans to expand to the USA in 2014.

• The service
We take the winery’s database, clean it up, and typically run 2 telesales campaigns per year. The timing, products and pricing are agreed with the winery prior to the campaign.
There are multiple benefits for the winery: the database is engaged with the winery, sales conversions are high and the database is reliable and up to date.

• The size of the company
Cellar Loop International employs about 20 people and plans to grow to 30. The turnover is in excess of AU$5m

• How long have you been established?
Cellar Loop was rebranded 12 months ago, but the original entity has been trading for 10 years.

• The company in a few words
Dynamic
Responsive
Detailed
Bright
Independent
Friendly
Engaging

The old web site

www.cellarloop.com.au

• What is good about the web site?
Clean look, succinct. No need to scroll down to get information.

• What don’t you like about the old web site?
Blocky top graphics look too cartoon-like
Stock photos
Dull, corporate look with no personality
Bad infographic on Services page
Limited contact information
Too much red

The new web site

• Outline the aims of the new web site
The main aim of the new website is to represent Cellar Loop and its personality better. We hope to be able to engage wineries to come back to the site. It has to contain the relevant service and benefit information to convert new winery business.

• Who is the target audience?
This is above all a B2B website aimed at winery partners
It is not an e-commerce site, but we want wineries to come back frequently.

• How will your target audience be accessing your site
All forms, probably including mobile phones.

• What are the unique selling points for your company, your products or your services?
Independent
Reliable
Secure

• Competitors' web sites:
www.vintrackers.com.au
http://www.morvellcasksupply.com.au/

The look and feel of the new web site

• Various web sites that we like the look & feel of.
http://www.tarbeck.com.au/ Great graphic on home page, good use of white space, uncluttered
http://pemvask.com/ Good use of space, clear navigation, bit quirky
http://www.casaorlen.com.au/ Ease of navigation, like the drop down “where we are” on the home page
http://www.starpilotnotes.co.uk/ Great use of graphics for navigation etc.

• Logo and sample of corporate identity files attached.

Wineries in Australia, NZ, Canada, USA

Nice to have
• Would be good to have a blog on the site to create new content easily and frequently

```html
<!DOCTYPE html>
<html lang="en">
<head>
<meta charset="utf-8">
<title>Cellar Loop – Uniting Wine &amp; People</title>
<link rel="stylesheet" href="https://fonts.googleapis.com/css2?family=Arimo:ital,wght@0,400;0,700;1,400;1,700&display=swap">
<style>
  :root {
    --brand-red: #e01b22;
    --brand-red-dark: #c8141b;
    --ink: #222222;
    --ink-soft: #333333;
    --nav-grey: #9a9a9a;
    --meta-grey: #8a8a8a;
    --page: #ffffff;
    --caption-bg: rgba(20, 18, 16, 0.82);
  }
  * { box-sizing: border-box; margin: 0; padding: 0; }
  html, body {
    width: 1200px; height: 821px; overflow: hidden;
    background: var(--page);
    font-family: "Arimo", Arial, sans-serif;
    color: var(--ink);
  }
  .page { position: relative; width: 1200px; height: 821px; }

  .brand {
    position: absolute; left: 84px; top: 58px;
    display: flex; align-items: center; gap: 12px;
  }
  .brand-mark { width: 18px; height: 18px; background: var(--brand-red); }
  .brand-name {
    font-weight: 400; font-size: 40px; line-height: 1;
    color: var(--brand-red);
  }

  .regions {
    position: absolute; right: 83px; top: 60px;
    display: flex; font-size: 13px; color: var(--meta-grey);
  }
  .regions span + span::before {
    content: "|"; margin: 0 9px; color: #b5b5b5;
  }

  .main-nav {
    position: absolute; top: 100px; left: 0; width: 1200px; height: 30px;
    font-size: 21px; color: var(--nav-grey);
  }
  .main-nav a { position: absolute; top: 0; color: inherit; text-decoration: none; }
  .main-nav a.is-current { color: var(--ink); }
  .nav-rule { position: absolute; left: 38px; top: 135px; width: 1125px; height: 2px; background: var(--brand-red); }
  .nav-marker { position: absolute; left: 422px; top: 126px; }

  .hero {
    position: absolute; left: 38px; top: 138px; width: 1125px; height: 354px;
    background:
      radial-gradient(ellipse at 85% 40%, #c9b8a4 0%, rgba(150,130,110,0) 40%),
      radial-gradient(ellipse at 20% 85%, #3e5a3a 0%, rgba(60,80,55,0) 35%),
      linear-gradient(100deg, #2c2620 0%, #6a5d52 35%, #8f8171 60%, #3b302a 100%);
  }
  .hero-caption {
    position: absolute; left: 1px; top: 176px; width: 558px; height: 58px;
    background: var(--caption-bg); color: #ffffff;
    font-size: 29px; line-height: 58px; padding-left: 30px;
  }
  .hero-caption strong { font-style: italic; font-weight: 700; font-size: 33px; }
  .hero-dots { position: absolute; left: 538px; top: 337px; display: flex; gap: 13px; }
  .hero-dots span { width: 7px; height: 7px; background: var(--brand-red); }
  .hero-dots span.is-active { width: 9px; height: 9px; margin-top: -1px; border: 1px solid #fff; }
  .hero-rule { position: absolute; left: 38px; top: 492px; width: 1125px; height: 2px; background: var(--brand-red); }

  .feature { position: absolute; top: 524px; width: 328px; }
  .feature h2 {
    font-weight: 400; font-size: 23px; color: var(--brand-red);
    padding-bottom: 6px; border-bottom: 2px solid var(--brand-red);
  }
  .feature p {
    margin-top: 6px; font-size: 17.2px; line-height: 24.6px; color: var(--ink-soft);
  }
  .feature a { color: var(--brand-red); font-style: italic; text-decoration: underline; margin-left: 6px; }
  .feature-wine { left: 36px; }
  .feature-craft { left: 437px; }
  .feature-international { left: 834px; }

  .site-footer {
    position: absolute; left: 38px; top: 765px; width: 1126px; height: 56px;
    background: linear-gradient(180deg, #e8242a 0%, var(--brand-red-dark) 100%);
    color: #ffffff;
  }
  .copyright { position: absolute; left: 24px; top: 22px; font-size: 11.5px; font-weight: 700; }
  .follow { position: absolute; right: 24px; top: 14px; display: flex; align-items: center; gap: 10px; }
  .follow-label { font-weight: 700; font-size: 15px; margin-right: 2px; }
  .social-badge { width: 26px; height: 26px; background: #ffffff; border-radius: 3px; opacity: 0.92; }
</style>
</head>
<body>
<div class="page">
  <div class="brand">
    <span class="brand-mark"></span>
    <span class="brand-name">Cellar Loop</span>
  </div>

  <div class="regions">
    <span>Australia</span><span>New Zealand</span><span>Hong Kong</span><span>Canada</span>
  </div>

  <nav class="main-nav">
    <a class="is-current" href="#" style="left:402px">Home</a>
    <a href="#" style="left:499px">About Us</a>
    <a href="#" style="left:631px">Services</a>
    <a href="#" style="left:754px">Benefits</a>
    <a href="#" style="left:874px">Testimonials</a>
    <a href="#" style="left:1040px">Contact</a>
  </nav>
  <svg class="nav-marker" width="22" height="11" viewBox="0 0 22 11"><polygon points="0,11 11,0 22,11" fill="#e01b22"/></svg>
  <div class="nav-rule"></div>

  <section class="hero" role="img" aria-label="Photo of a man in glasses smelling white wine from a glass at a tasting event">
    <div class="hero-caption"><strong>Cellar Loop</strong> Uniting Wine &amp; People</div>
    <div class="hero-dots"><span></span><span class="is-active"></span><span></span></div>
  </section>
  <div class="hero-rule"></div>

  <article class="feature feature-wine">
    <h2>Your Wine.</h2>
    <p>We sell it like we made it.When your customers are contacted by Cellar Loop, they will feel as <a href="#">Read more.</a></p>
  </article>
  <article class="feature feature-craft">
    <h2>You make great wine.</h2>
    <p>Our staff are highly trained in every aspect of your products and learn the values of your brand and what it represents. When your customers are contacted by Cellar Loop, they will feel as if they had just spoken with a member of your own team. <a href="#">Read more.</a></p>
  </article>
  <article class="feature feature-international">
    <h2>Cellar Loop International.</h2>
    <p>Cellar Loop is the first agency offering international service. We have offices in Australia, New Zealand and Canada. Ask us how we can help you in these countries and more. <a href="#">Read more.</a></p>
  </article>

  <footer class="site-footer">
    <div class="copyright">© Copyright 2013. All right reserved.</div>
    <div class="follow">
      <span class="follow-label">Follow Us:</span>
      <span class="social-badge" aria-label="Video channel"></span>
      <span class="social-badge" aria-label="Microblog"></span>
      <span class="social-badge" aria-label="Social network"></span>
    </div>
  </footer>
</div>
</body>
</html>
```